San Francisco Pet Care Non Profit

Business Card Design for non profit organization.
We are a mobile pet care team who supports and attends to pets whose owners are homeless. Thanks for your help and creativity.

Industry/Entity Type

Non Profit

Contact Information for Business Card

Miriam Loxley
President
2817 Harrow Street, #516
San Francisco, CA 94187
phone: 415-782-3946
fax: 415-718-4053
miriam@warmpawvan.org
website: warmpawvan.org
facebook: friendloop.com/WarmPawVan

Font styles to use
Serif
Sans Serif

Colors

Designer to choose colors to be used in the design.

Requirements
Must have
• above details and attached logo

```html
<!DOCTYPE html>
<html lang="en">
<head>
<meta charset="utf-8">
<title>WarmPawVan Business Card</title>
<link rel="stylesheet" href="https://fonts.googleapis.com/css2?family=Montserrat:wght@400;500;600&family=Work+Sans:wght@400;500&display=swap">
<style>
  :root {
    --page: #d9dadb;
    --card: #202123;
    --card-deep: #17181a;
    --accent: #29a8e0;
    --ink-light: #f2f2f2;
    --band-top: #38393b;
    --band-bottom: #141516;
    --band-text: #4a4b4e;
    --pattern-a: #2a2b2d;
    --pattern-b: #1c1d1f;
  }
  * { box-sizing: border-box; margin: 0; padding: 0; }
  html, body { width: 1200px; height: 900px; overflow: hidden; }
  body {
    background: var(--page);
    font-family: "Work Sans", Arial, sans-serif;
    display: flex;
    flex-direction: column;
    align-items: center;
    justify-content: center;
    gap: 40px;
  }
  .card {
    position: relative;
    width: 680px;
    height: 388px;
    background: var(--card);
    overflow: hidden;
  }

  /* Front */
  .card-front {
    border-left: 6px solid var(--accent);
    border-bottom: 6px solid var(--accent);
  }
  .brand {
    position: absolute;
    top: 42px;
    right: 48px;
    display: flex;
    align-items: center;
    gap: 12px;
  }
  .brand-dot {
    width: 38px;
    height: 38px;
    border-radius: 50%;
    background: var(--accent);
  }
  .brand-text { display: flex; flex-direction: column; }
  .brand-name {
    font-family: "Montserrat", Arial, sans-serif;
    font-weight: 600;
    font-size: 30px;
    line-height: 1;
    color: var(--accent);
  }
  .brand-tagline {
    font-family: "Montserrat", Arial, sans-serif;
    font-weight: 600;
    font-size: 11px;
    color: var(--ink-light);
    text-align: right;
    margin-top: 3px;
  }
  .person-name {
    position: absolute;
    left: 40px;
    top: 124px;
    font-family: "Montserrat", Arial, sans-serif;
    font-weight: 500;
    font-size: 27px;
    letter-spacing: 2px;
    color: var(--accent);
    text-transform: uppercase;
  }
  .divider {
    position: absolute;
    left: 40px;
    right: 48px;
    top: 160px;
    height: 2px;
    background: var(--accent);
  }
  .person-role {
    position: absolute;
    left: 40px;
    top: 168px;
    font-size: 15px;
    letter-spacing: 1px;
    color: var(--ink-light);
  }
  .contact-list {
    position: absolute;
    left: 40px;
    top: 208px;
    list-style: none;
  }
  .contact-item {
    display: flex;
    align-items: center;
    gap: 12px;
    font-size: 15px;
    letter-spacing: 1px;
    line-height: 28px;
    color: var(--ink-light);
  }
  .contact-icon { width: 13px; height: 13px; flex: none; }
  .address {
    position: absolute;
    right: 48px;
    bottom: 42px;
    text-align: right;
    font-style: normal;
    font-size: 15px;
    letter-spacing: 1px;
    line-height: 26px;
    color: var(--ink-light);
  }

  /* Back */
  .card-back { background: var(--card-deep); }
  .pattern-field {
    position: absolute;
    inset: 0;
    background: linear-gradient(135deg, var(--pattern-b), var(--pattern-a) 55%, var(--pattern-b));
  }
  .name-band {
    position: absolute;
    left: 0;
    right: 0;
    top: 150px;
    height: 92px;
    background: linear-gradient(to bottom, var(--band-top) 0 50%, var(--band-bottom) 50% 100%);
    display: flex;
    flex-direction: column;
    align-items: center;
    justify-content: center;
  }
  .band-name {
    font-family: "Montserrat", Arial, sans-serif;
    font-weight: 600;
    font-size: 44px;
    line-height: 1;
    color: var(--band-text);
  }
  .band-tagline {
    font-family: "Montserrat", Arial, sans-serif;
    font-weight: 600;
    font-size: 16px;
    color: var(--band-text);
    margin-top: 4px;
  }
</style>
</head>
<body>

  <section class="card card-front">
    <div class="brand">
      <span class="brand-dot"></span>
      <div class="brand-text">
        <span class="brand-name">WarmPawVan</span>
        <span class="brand-tagline">Mobile Pet Care Team</span>
      </div>
    </div>

    <h1 class="person-name">Miriam Loxley</h1>
    <div class="divider"></div>
    <p class="person-role">President</p>

    <ul class="contact-list">
      <li class="contact-item">
        <svg class="contact-icon" viewBox="0 0 16 16"><path fill="#29a8e0" d="M3.5 1l2.5 3-1.5 1.6c.8 2 2.4 3.6 4.4 4.4L10.5 8.5l3 2.5-1.6 2.8C7 13.5 2.5 9 2.2 4.1z"/></svg>
        415-782-3946
      </li>
      <li class="contact-item">
        <svg class="contact-icon" viewBox="0 0 16 16"><rect x="4" y="1" width="8" height="5" fill="none" stroke="#29a8e0" stroke-width="1.5"/><rect x="1" y="6" width="14" height="6" rx="1" fill="#29a8e0"/><rect x="4" y="10" width="8" height="5" fill="#202123" stroke="#29a8e0" stroke-width="1.5"/></svg>
        415-718-4053
      </li>
      <li class="contact-item">
        <svg class="contact-icon" viewBox="0 0 16 16"><rect x="1" y="3" width="14" height="10" fill="none" stroke="#29a8e0" stroke-width="1.5"/><path d="M1 3l7 6 7-6" fill="none" stroke="#29a8e0" stroke-width="1.5"/></svg>
        miriam@warmpawvan.org
      </li>
      <li class="contact-item">
        <svg class="contact-icon" viewBox="0 0 16 16"><circle cx="8" cy="8" r="6.5" fill="none" stroke="#29a8e0" stroke-width="1.5"/><ellipse cx="8" cy="8" rx="3" ry="6.5" fill="none" stroke="#29a8e0" stroke-width="1.2"/><path d="M1.5 8h13" stroke="#29a8e0" stroke-width="1.2"/></svg>
        www.warmpawvan.org
      </li>
      <li class="contact-item">
        <svg class="contact-icon" viewBox="0 0 16 16"><circle cx="8" cy="8" r="7" fill="#29a8e0"/></svg>
        friendloop.com/WarmPawVan
      </li>
    </ul>

    <address class="address">
      2817 Harrow Street, #516<br>
      San Francisco, CA 94187
    </address>
  </section>

  <section class="card card-back">
    <div class="pattern-field" role="img" aria-label="Repeating pattern of the organisation's pet emblem across the card"></div>
    <div class="name-band">
      <span class="band-name">WarmPawVan</span>
      <span class="band-tagline">Mobile Pet Care Team</span>
    </div>
  </section>

</body>
</html>
```